Brightfold Partners Website

Brightfold Partners Advisory Services is a company which provides specialised advise in carbon markets, climate policy, landscapes, resilience and change. We are based in Australia but the majority of our business is global. Our clients range from governments to large corporates and not for profit organisations.
Our focus is on developing the capabilities of government officials, business decision makers and land managers so they can better navigate the complexity of climate change and sustainability.
We are looking for a website that is consistent with the high end professional services which we provide to serious players.
I have attached two versions of our logo. I have also attached the back of our business card so you can get a sense of what we hand to potential clients.

Target Market(s)

Professional individuals, decision makers, board members etc, government officials.

Industry/Entity Type

Government

Number of Pages Required

4 page

Font styles to use
Serif
Sans Serif

Requirements
Must have
• Please provide
• 1. Home page
• 2. Service page template
• 3. Contact page
• 4. Lead expert profile page

```html
<!DOCTYPE html>
<html lang="en">
<head>
<meta charset="utf-8">
<title>Brightfold Partners Website</title>
<link rel="stylesheet" href="https://fonts.googleapis.com/css2?family=Cormorant+Garamond:wght@500&family=Lora:wght@400;700&family=Open+Sans:wght@400&display=swap">
<style>
  :root {
    --ink: #1f2a33;
    --white: #ffffff;
    --muted: #8a9096;
    --rule: #d9dcdf;
    --field: #eef0f1;
    --button: #2c3236;
    --legal: #4a5157;
    --social: #5b6c78;
  }
  * { box-sizing: border-box; margin: 0; padding: 0; }
  html, body { width: 820px; height: 1200px; overflow: hidden; background: var(--white); }
  body { position: relative; font-family: "Lora", Georgia, serif; color: var(--ink); }

  .hero { position: absolute; left: 0; top: 0; width: 820px; height: 418px; overflow: hidden; }
  .hero-photo {
    position: absolute; inset: 0;
    background:
      radial-gradient(ellipse 180px 260px at 430px 230px, rgba(40,52,60,.55), rgba(40,52,60,0) 70%),
      radial-gradient(ellipse 160px 200px at 240px 300px, rgba(200,208,212,.35), rgba(200,208,212,0) 70%),
      radial-gradient(ellipse 140px 220px at 780px 300px, rgba(215,205,200,.35), rgba(215,205,200,0) 70%),
      radial-gradient(ellipse 120px 260px at 30px 260px, rgba(60,70,78,.45), rgba(60,70,78,0) 70%),
      linear-gradient(90deg, #7d8a91 0%, #8f9ba1 30%, #66747c 55%, #86939a 80%, #939ea3 100%);
  }
  .hero-shade { position: absolute; inset: 0; background: linear-gradient(180deg, rgba(40,52,60,.25), rgba(40,52,60,.1) 40%, rgba(40,52,60,.35)); }
  .social-top { position: absolute; left: 116px; top: 17px; display: flex; gap: 11px; }
  .social-top span { width: 8px; height: 8px; border-radius: 50%; background: rgba(255,255,255,.75); }
  .main-nav { position: absolute; top: 18px; right: 120px; display: flex; gap: 24px; }
  .main-nav a { color: var(--white); text-decoration: none; font-size: 10.5px; letter-spacing: .2px; }
  .brand-ring { position: absolute; left: 361px; top: 86px; width: 96px; height: 96px; border-radius: 50%; border: 1.5px solid rgba(255,255,255,.85); background: rgba(255,255,255,.1); }
  .brand-rule { position: absolute; left: 293px; width: 232px; height: 1px; background: rgba(255,255,255,.6); }
  .brand-name {
    position: absolute; left: 250px; top: 209px; width: 320px; text-align: center;
    font-family: "Cormorant Garamond", Georgia, serif; font-weight: 500; color: var(--white);
    font-size: 31px; line-height: 34px; letter-spacing: 3px;
  }
  .hero-contact { position: absolute; top: 300px; font-family: "Open Sans", Arial, sans-serif; font-size: 8.5px; color: var(--white); display: flex; align-items: center; gap: 5px; }
  .scroll-down { position: absolute; left: 390px; top: 357px; }

  .welcome { position: absolute; left: 0; top: 445px; width: 820px; text-align: center; }
  .welcome h1 { font-size: 16.5px; font-weight: 700; letter-spacing: .3px; }
  .welcome p {
    margin: 3px auto 0; width: 352px; display: flex; align-items: center; gap: 8px;
    font-family: "Open Sans", Arial, sans-serif; font-size: 9.5px; color: var(--muted);
  }
  .welcome p::before, .welcome p::after { content: ""; flex: 1; height: 1px; background: var(--rule); }

  .services { position: absolute; left: 117px; top: 508px; display: grid; grid-template-columns: 289px 289px; grid-auto-rows: 156px; gap: 6px 7px; }
  .service-tile { position: relative; display: flex; align-items: center; justify-content: center; }
  .tile-carbon {
    background:
      radial-gradient(ellipse 90px 110px at 250px 90px, rgba(35,45,60,.55), rgba(35,45,60,0) 70%),
      radial-gradient(ellipse 80px 90px at 60px 110px, rgba(50,60,72,.5), rgba(50,60,72,0) 70%),
      linear-gradient(160deg, #a7b7c2 0%, #7f93a2 50%, #51606d 100%);
  }
  .tile-landscapes {
    background:
      radial-gradient(ellipse 110px 60px at 180px 110px, rgba(225,230,232,.6), rgba(225,230,232,0) 70%),
      radial-gradient(ellipse 80px 100px at 30px 40px, rgba(80,95,110,.45), rgba(80,95,110,0) 70%),
      linear-gradient(180deg, #8f9ca6 0%, #aab5bb 55%, #c3cacd 100%);
  }
  .tile-policy {
    background:
      radial-gradient(ellipse 70px 80px at 120px 90px, rgba(150,90,95,.4), rgba(150,90,95,0) 70%),
      radial-gradient(ellipse 80px 100px at 240px 80px, rgba(60,70,85,.45), rgba(60,70,85,0) 70%),
      linear-gradient(180deg, #8d9aa3 0%, #a0acb2 55%, #b8c0c3 100%);
  }
  .tile-resilience {
    background:
      radial-gradient(ellipse 90px 110px at 250px 100px, rgba(35,38,44,.6), rgba(35,38,44,0) 70%),
      radial-gradient(ellipse 80px 90px at 60px 60px, rgba(200,195,185,.45), rgba(200,195,185,0) 70%),
      linear-gradient(170deg, #9a9fa3 0%, #7f878d 55%, #5d656b 100%);
  }
  .service-tile h2 { color: var(--white); font-size: 15.5px; font-weight: 700; padding: 14px 0; width: 170px; text-align: center; border-top: 1px solid rgba(255,255,255,.55); border-bottom: 1px solid rgba(255,255,255,.55); white-space: nowrap; text-shadow: 0 1px 2px rgba(0,0,0,.25); }

  .contact-band {
    position: absolute; left: 0; top: 867px; width: 820px; height: 268px;
    background:
      radial-gradient(ellipse 80px 100px at 755px 110px, rgba(225,235,238,.45), rgba(225,235,238,0) 70%),
      radial-gradient(ellipse 260px 60px at 420px 240px, rgba(30,40,48,.5), rgba(30,40,48,0) 70%),
      radial-gradient(ellipse 200px 80px at 120px 200px, rgba(215,222,225,.4), rgba(215,222,225,0) 70%),
      linear-gradient(180deg, #7f8d92 0%, #6e8087 45%, #5a6a70 100%);
  }
  .contact-head { position: absolute; left: 286px; top: 896px; display: flex; align-items: center; gap: 12px; }
  .contact-head .ring { width: 48px; height: 48px; border-radius: 50%; border: 1.5px solid rgba(255,255,255,.9); background: rgba(255,255,255,.12); }
  .contact-head h2 { color: var(--white); font-size: 18.5px; font-weight: 700; }
  .field { position: absolute; background: var(--field); opacity: .93; font-size: 8px; color: #555d63; padding: 10px 12px; letter-spacing: .3px; }
  .send { position: absolute; left: 198px; top: 1076px; width: 423px; height: 30px; background: var(--button); color: var(--white); font-size: 9px; text-align: center; line-height: 30px; letter-spacing: .5px; }

  .site-footer { position: absolute; left: 0; top: 1135px; width: 820px; height: 65px; }
  .site-footer .legal { position: absolute; left: 120px; top: 26px; font-size: 9.5px; color: var(--legal); }
  .site-footer .footer-name { position: absolute; left: 340px; top: 26px; width: 140px; text-align: center; font-size: 9.5px; color: var(--legal); letter-spacing: 1px; }
  .social-foot { position: absolute; left: 603px; top: 22px; display: flex; gap: 8px; }
  .social-foot span { width: 19px; height: 19px; border-radius: 50%; background: var(--social); }
</style>
</head>
<body>
  <header class="hero">
    <div class="hero-photo" role="img" aria-label="Photo of advisers meeting with clients in a bright office"></div>
    <div class="hero-shade"></div>
    <div class="social-top"><span></span><span></span><span></span><span></span></div>
    <nav class="main-nav"><a href="#">HOME</a><a href="#">SERVICES</a><a href="#">PROFILE</a><a href="#">CONTACT</a></nav>
    <div class="brand-ring"></div>
    <div class="brand-rule" style="top:201px"></div>
    <div class="brand-name">BRIGHTFOLD<br>PARTNERS</div>
    <div class="brand-rule" style="top:285px"></div>
    <div class="hero-contact" style="left:294px">
      <svg width="11" height="11" viewBox="0 0 12 12"><path d="M2 1.5l2 .3.7 2-1.2 1a6 6 0 0 0 3.7 3.7l1-1.2 2 .7.3 2c-4.6.6-9.1-3.9-8.5-8.5z" fill="none" stroke="#fff" stroke-width="1"/></svg>
      <span>0800 (555) 0192</span>
    </div>
    <div class="hero-contact" style="left:410px">
      <svg width="13" height="10" viewBox="0 0 13 10"><rect x=".5" y=".5" width="12" height="9" fill="none" stroke="#fff"/><path d="M.5 .5l6 5 6-5" fill="none" stroke="#fff"/></svg>
      <span>info@brightfoldpartners.example</span>
    </div>
    <svg class="scroll-down" width="40" height="40" viewBox="0 0 40 40"><circle cx="20" cy="20" r="19" fill="none" stroke="rgba(255,255,255,.75)"/><path d="M13 17l7 6 7-6" fill="none" stroke="#fff" stroke-width="1.2"/></svg>
  </header>

  <section class="welcome">
    <h1>WELCOME TO THE BRIGHTFOLD PARTNERS !</h1>
    <p>Brightfold Partners Advisory Services</p>
  </section>

  <section class="services">
    <div class="service-tile tile-carbon" role="img" aria-label="Photo of a team looking toward a presentation"><h2>CARBON MARKETS</h2></div>
    <div class="service-tile tile-landscapes" role="img" aria-label="Photo of a hand signing a document"><h2>LANDSCAPES</h2></div>
    <div class="service-tile tile-policy" role="img" aria-label="Photo of colleagues around a meeting table"><h2>CLIMATE POLICY</h2></div>
    <div class="service-tile tile-resilience" role="img" aria-label="Photo of people reviewing papers together"><h2>RESILIENCE</h2></div>
  </section>

  <section class="contact-band" role="img" aria-label="Photo of a meeting table with papers, glasses and a pen"></section>
  <div class="contact-head"><div class="ring"></div><h2>CONTACT US NOW !</h2></div>
  <div class="field" style="left:198px;top:962px;width:209px;height:29px">NAME</div>
  <div class="field" style="left:411px;top:962px;width:210px;height:29px">EMAIL</div>
  <div class="field" style="left:198px;top:995px;width:423px;height:77px">MESSAGE</div>
  <div class="send">SEND</div>

  <footer class="site-footer">
    <div class="legal">Brightfold Partners © 2014 Privacy Policy</div>
    <div class="footer-name">BRIGHTFOLD</div>
    <div class="social-foot"><span></span><span></span><span></span><span></span></div>
  </footer>
</body>
</html>
```